Business cards design on a high standard

We advise clients on insurance and financial matters, since these clients pay for our advice, the design should have a high standard. Our logo should be included. From the colors we are open for everything.

Colors

Designer to choose colors to be used in the design.

```html
<!DOCTYPE html>
<html lang="en">
<head>
<meta charset="utf-8">
<title>Keller Advisory business cards</title>
<link href="https://fonts.googleapis.com/css2?family=Oswald:wght@500&family=Roboto:wght@300;400;700&display=swap" rel="stylesheet">
<style>
  :root {
    --backdrop: #3a3a3c;
    --card: #2a2a2b;
    --accent: #e0222b;
    --ink: #f2f2f2;
    --ink-soft: #d9d9d9;
  }
  * { margin: 0; padding: 0; box-sizing: border-box; }
  html, body { width: 1200px; height: 901px; overflow: hidden; }
  body {
    background: var(--backdrop);
    font-family: "Roboto", Arial, sans-serif;
    position: relative;
  }
  .card {
    position: absolute;
    left: 285px;
    width: 630px;
    height: 360px;
    background: var(--card);
    box-shadow: 0 10px 30px rgba(0,0,0,.35);
    overflow: hidden;
  }
  .card::after {
    content: "";
    position: absolute;
    left: 0; right: 0; bottom: 0;
    height: 11px;
    background: var(--accent);
  }
  .card--front { top: 75px; }
  .card--back { top: 465px; }

  .brand {
    position: absolute;
    left: 0; right: 0; top: 140px;
    text-align: center;
    color: var(--ink);
    font-weight: 700;
    font-size: 50px;
    letter-spacing: 4px;
    text-transform: uppercase;
  }

  .identity {
    position: absolute;
    right: 360px;
    top: 128px;
    text-align: right;
  }
  .identity__name {
    font-family: "Oswald", "Arial Narrow", sans-serif;
    font-weight: 500;
    font-size: 40px;
    line-height: 1;
    color: var(--accent);
    text-transform: uppercase;
    letter-spacing: -0.5px;
  }
  .identity__role {
    font-weight: 300;
    font-size: 22px;
    color: var(--ink-soft);
    margin-top: 4px;
  }
  .divider {
    position: absolute;
    left: 300px;
    top: 125px;
    width: 2px;
    height: 80px;
    background: var(--ink-soft);
  }
  .contacts {
    position: absolute;
    left: 326px;
    top: 130px;
    list-style: none;
  }
  .contacts li {
    display: flex;
    align-items: center;
    gap: 10px;
    font-weight: 400;
    font-size: 20px;
    color: var(--ink);
    line-height: 26px;
  }
  .contacts svg { width: 16px; height: 16px; fill: var(--accent); flex: none; }
  .contacts .highlight { color: var(--accent); }
  .address {
    position: absolute;
    left: 0; right: 0; bottom: 52px;
    text-align: center;
    font-weight: 300;
    font-size: 21px;
    color: var(--ink);
  }
</style>
</head>
<body>
  <section class="card card--front">
    <div class="brand">Keller Advisory</div>
  </section>

  <section class="card card--back">
    <div class="identity">
      <div class="identity__name">Martin Keller</div>
      <div class="identity__role">Manager</div>
    </div>
    <div class="divider"></div>
    <ul class="contacts">
      <li>
        <svg viewBox="0 0 16 16" aria-hidden="true"><path d="M3.5 1l2.5 3-1.5 1.8c.8 2 2.3 3.5 4.2 4.3L10.5 8.6l3 2.5-1.6 3c-5.6-.5-10-4.9-10.5-10.5z"/></svg>
        555-014-2100
      </li>
      <li>
        <svg viewBox="0 0 16 16" aria-hidden="true"><path d="M1 4h14v9H1z M1 4l7 5 7-5" fill="none" stroke="#e0222b" stroke-width="1.6"/></svg>
        martin@kelleradvisory.com
      </li>
      <li>
        <svg viewBox="0 0 16 16" aria-hidden="true"><circle cx="8" cy="8" r="6.5" fill="none" stroke="#e0222b" stroke-width="1.6"/><path d="M1.5 8h13M8 1.5c-3 3.5-3 9.5 0 13M8 1.5c3 3.5 3 9.5 0 13" fill="none" stroke="#e0222b" stroke-width="1.2"/></svg>
        <span>www.<span class="highlight">kelleradvisory</span>.com</span>
      </li>
    </ul>
    <div class="address">Your address, city, state, ZIP 0000</div>
  </section>
</body>
</html>
```